We sell companies excess stock for them

We need a business card for a company based in New Zealand called 'StockHarbor'.

Check out our website to get an idea www.stockharbor.example

We help other businesses to;
- Sell Excess Stock
- Manage Product Returns
- Sell Company Assets

Our logo is attached for your reference
The font used is 'RifficFree-Bold'

Target Market(s)

Businesses

Industry/Entity Type

Business

Contact Information for Business Card

Name: Mark Pellow
Phone: 027 846 2093
email: markpellow@stockharbor.example
website: www.stockharbor.example

Font styles to use
Other font styles liked:
• Unsure

Colors
9bcb3b

Requirements
Must have
• coming soon
Nice to have
• coming soon
Should not have
• coming soon

```html
<!DOCTYPE html>
<html lang="en">
<head>
<meta charset="utf-8">
<title>StockHarbor Business Card</title>
<link rel="stylesheet" href="https://fonts.googleapis.com/css2?family=Open+Sans:wght@400;600;700&family=Nunito:wght@800;900&display=swap">
<style>
  :root {
    --bg: #e6e7e9;
    --card: #ffffff;
    --ink: #1c1c1c;
    --green: #9bcb3b;
    --green-deep: #86b52b;
    --band-text: #ffffff;
    --shadow: rgba(0,0,0,0.18);
  }
  * { margin: 0; padding: 0; box-sizing: border-box; }
  html, body {
    width: 1200px; height: 900px; overflow: hidden;
    background: var(--bg);
  }
  .stage { position: relative; width: 1200px; height: 900px; }
  .card {
    position: absolute;
    left: 290px;
    width: 620px; height: 354px;
    background: var(--card);
    border-radius: 22px;
    overflow: hidden;
    box-shadow: 0 10px 30px var(--shadow);
  }
  .card--front { top: 70px; }
  .card--back { top: 476px; }

  .wordmark {
    font-family: "Open Sans", sans-serif;
    font-weight: 700;
    color: var(--ink);
    letter-spacing: -1px;
    line-height: 1;
  }
  .card--front .wordmark {
    position: absolute; left: 0; right: 0; top: 150px;
    text-align: center; font-size: 52px;
  }
  .card--back .wordmark {
    position: absolute; left: 40px; top: 36px;
    font-size: 46px;
  }

  .contact {
    position: absolute; left: 44px; top: 100px;
    font-family: "Open Sans", sans-serif;
    color: var(--ink);
  }
  .contact__name { font-size: 16px; font-weight: 600; line-height: 22px; }
  .contact__role { font-size: 16px; font-weight: 700; line-height: 22px; color: var(--green); }
  .contact__list { list-style: none; margin-top: 4px; }
  .contact__item {
    display: flex; align-items: center; gap: 8px;
    font-size: 16px; font-weight: 600; line-height: 22px;
  }
  .contact__icon { width: 16px; height: 16px; flex: none; }

  .mascot {
    position: absolute; left: 440px; top: 22px;
    width: 150px; height: 150px;
    border-radius: 50%;
    background: radial-gradient(circle at 45% 40%, #f3b24a 0%, #c6df8c 55%, rgba(155,203,59,0.15) 75%, rgba(255,255,255,0) 76%);
  }

  .band { position: absolute; left: 0; bottom: 0; width: 620px; height: 158px; }
  .band__text {
    position: absolute; left: 40px; bottom: 24px;
    font-family: "Nunito", sans-serif;
    font-weight: 900;
    font-size: 19px;
    line-height: 26px;
    color: var(--band-text);
  }
</style>
</head>
<body>
<main class="stage">
  <section class="card card--front">
    <p class="wordmark">StockHarbor</p>
  </section>

  <section class="card card--back">
    <p class="wordmark">StockHarbor</p>

    <div class="mascot" role="img" aria-label="Cartoon delivery mascot in green cap and overalls carrying an orange parcel, giving a thumbs up"></div>

    <div class="contact">
      <p class="contact__name">Mark Pellow</p>
      <p class="contact__role">managing director</p>
      <ul class="contact__list">
        <li class="contact__item">
          <svg class="contact__icon" viewBox="0 0 18 18" aria-hidden="true">
            <rect x="1" y="1" width="16" height="16" rx="4" fill="none" stroke="var(--green)" stroke-width="2"/>
            <path d="M5.5 7.5c0-1.5 7-1.5 7 0v1h-2v-1h-3v1h-2z M6 10h6v2H6z" fill="var(--ink)"/>
          </svg>
          027 846 2093
        </li>
        <li class="contact__item">
          <svg class="contact__icon" viewBox="0 0 18 18" aria-hidden="true">
            <rect x="1" y="1" width="16" height="16" rx="4" fill="none" stroke="var(--green)" stroke-width="2"/>
            <rect x="4.5" y="5.5" width="9" height="7" fill="none" stroke="var(--ink)" stroke-width="1.5"/>
            <path d="M4.5 5.5l4.5 4 4.5-4" fill="none" stroke="var(--ink)" stroke-width="1.5"/>
          </svg>
          markpellow@stockharbor.example
        </li>
        <li class="contact__item">
          <svg class="contact__icon" viewBox="0 0 18 18" aria-hidden="true">
            <rect x="1" y="1" width="16" height="16" rx="4" fill="none" stroke="var(--green)" stroke-width="2"/>
            <circle cx="9" cy="9" r="4.5" fill="none" stroke="var(--ink)" stroke-width="1.3"/>
            <path d="M4.5 9h9M9 4.5c-2 2.5-2 6.5 0 9M9 4.5c2 2.5 2 6.5 0 9" fill="none" stroke="var(--ink)" stroke-width="1.1"/>
          </svg>
          www.stockharbor.example
        </li>
      </ul>
    </div>

    <svg class="band" viewBox="0 0 620 158" preserveAspectRatio="none" aria-hidden="true">
      <path d="M0 40 C 200 34, 420 18, 620 0 L620 158 L0 158 Z" fill="var(--green)"/>
      <path d="M0 40 C 200 34, 420 18, 620 0" fill="none" stroke="var(--green-deep)" stroke-width="2"/>
    </svg>
    <p class="band__text">Selling Excess Stock • Managing Product Returns<br>Selling Company Assets</p>
  </section>
</main>
</body>
</html>
```